Electrician Company Website Design

I am looking to get a website designed only. I do not need it converted ot html. I simply need the design in a psd format. I have my own team for the conversion. The website is for an electrician company called Bramblecourt electric. I have created a txt document with the project parameters and specifics. I have also uploaded their logo in all avaible formats. It's a zip file.

Number of Pages Required

1 page

```html
<!DOCTYPE html>
<html lang="en">
<head>
<meta charset="utf-8">
<title>Bramblecourt Electric</title>
<link href="https://fonts.googleapis.com/css2?family=Oswald:wght@300;400;500;700&family=Lato:wght@400;700&display=swap" rel="stylesheet">
<style>
:root{
  --blue:#1f6bbb;
  --blue-dark:#174f8c;
  --red:#a3201f;
  --red-dark:#7f1716;
  --ink:#231f20;
  --text:#333;
  --white:#fff;
  --grey:#e9e9e9;
}
*{margin:0;padding:0;box-sizing:border-box}
html,body{width:1200px;height:4507px;overflow:hidden}
body{position:relative;background:var(--white);font-family:'Lato',sans-serif;color:var(--text)}
.abs{position:absolute}
.ph{position:absolute}
/* header */
.site-header{position:absolute;left:0;top:0;width:1200px;height:115px;background:var(--white)}
.brand{position:absolute;left:100px;top:28px;display:flex;align-items:center;gap:10px;font-family:'Oswald',sans-serif;font-weight:700;font-size:22px;color:var(--blue-dark);text-transform:uppercase;letter-spacing:.5px}
.brand-dot{width:34px;height:34px;border-radius:50%;background:var(--red)}
.phone-tab{position:absolute;left:950px;top:0;width:250px;height:36px;background:var(--blue-dark);color:#fff;font-family:'Oswald',sans-serif;font-size:17px;display:flex;align-items:center;padding-left:36px;gap:8px;clip-path:polygon(8% 0,100% 0,100% 100%,0 100%)}
.main-nav{position:absolute;right:100px;top:60px;display:flex;gap:50px;font-family:'Oswald',sans-serif;font-size:16px;color:var(--ink);text-transform:uppercase}
/* hero */
.hero{position:absolute;left:0;top:115px;width:1200px;height:532px;background:linear-gradient(100deg,#8f9397 0%,#b7b9bb 40%,#8c8f93 70%,#5d6167 100%)}
.hero-title{position:absolute;left:157px;top:190px;color:#fff;font-family:'Oswald',sans-serif;line-height:1.05;white-space:nowrap}
.hero-title .light{font-weight:300;font-size:74px;display:block}
.hero-title .bold{font-weight:700;font-size:76px;display:block}
.hero-lead{position:absolute;left:160px;top:362px;width:420px;color:#fff;font-size:17px;line-height:1.65}
.btn{position:absolute;height:44px;background:var(--red);color:#fff;font-family:'Oswald',sans-serif;font-weight:500;font-size:15px;text-transform:uppercase;display:flex;align-items:center;padding:0 30px 0 36px;gap:6px;white-space:nowrap}
.arrow{position:absolute;top:300px}
/* info boxes */
.info{position:absolute;top:631px;height:184px;width:334px;color:#fff;padding:28px 20px 0 86px}
.info h3{font-family:'Oswald',sans-serif;font-weight:500;font-size:18px;text-transform:uppercase;margin-bottom:6px}
.info p{font-size:14.5px;line-height:1.65}
.info svg{position:absolute;left:26px;top:28px}
/* welcome */
.welcome-frame{position:absolute;left:110px;top:878px;width:486px;height:383px;border:2px solid var(--blue);border-radius:8px}
.welcome-photo{left:100px;top:892px;width:486px;height:383px;border-radius:8px;background:linear-gradient(135deg,#f2f2f0 0%,#dcdcd8 50%,#b8aa92 100%)}
.eyebrow{font-family:'Oswald',sans-serif;font-weight:400;font-size:22px;color:var(--red);text-transform:uppercase}
.section-title{font-family:'Oswald',sans-serif;color:var(--ink);text-transform:uppercase}
.section-title .l{font-weight:300}
.section-title .b{font-weight:700}
.body-copy{font-size:15.5px;line-height:1.75;color:#333}
/* services */
.service-card{position:absolute;width:490px;height:338px;display:flex;flex-direction:column;align-items:center;justify-content:center;color:#fff;font-family:'Oswald',sans-serif;font-size:27px;text-align:center;line-height:1.3}
.service-card span{margin-top:8px}
/* service area */
.area-list{position:absolute;left:100px;top:2660px;width:520px;display:flex;flex-wrap:wrap;column-gap:54px;row-gap:34px;font-size:20px;color:var(--blue)}
.area-list div{display:flex;align-items:center;gap:10px}
/* quote */
.quote{position:absolute;left:775px;top:3005px;width:325px;height:402px;background:var(--red);padding:14px 16px}
.quote h3{font-family:'Oswald',sans-serif;color:#fff;font-size:30px;font-weight:300;text-transform:uppercase;margin-bottom:14px}
.quote h3 b{font-weight:700}
.field{height:38px;background:#fff;margin-bottom:9px;font-size:15px;color:#555;padding:8px 8px}
.quote-btn{display:inline-flex;align-items:center;height:44px;border:2px solid #fff;color:#fff;font-family:'Oswald',sans-serif;font-weight:500;font-size:15px;padding:0 20px;margin-top:14px;gap:6px}
/* footer */
.footer{position:absolute;left:0;top:4098px;width:1200px;height:409px;background:var(--ink);color:#cfcfcf}
.footer h4{font-family:'Oswald',sans-serif;font-weight:500;font-size:15px;color:#fff;text-transform:uppercase;margin-bottom:20px}
.fcol{position:absolute;top:70px;font-size:15px;line-height:2.3}
.fdiv{position:absolute;top:85px;width:2px;height:180px;background:#fff;opacity:.8}
.footer-brand{position:absolute;left:100px;top:130px;width:180px;display:flex;flex-direction:column;align-items:center;gap:10px;font-family:'Oswald',sans-serif;font-weight:700;font-size:18px;line-height:1.2;color:#fff;text-transform:uppercase;text-align:center}
.footer-brand .dot{width:40px;height:40px;border-radius:50%;background:#fff}
.social{display:flex;gap:12px}
.social span{width:32px;height:32px;border-radius:50%;background:#fff}
</style>
</head>
<body>

<header class="site-header">
  <div class="brand"><span class="brand-dot"></span>Bramblecourt Electric</div>
  <div class="phone-tab">
    <svg width="16" height="16" viewBox="0 0 24 24"><path fill="#fff" d="M6.6 10.8a15 15 0 006.6 6.6l2.2-2.2c.3-.3.7-.4 1-.2 1.1.4 2.3.6 3.6.6.6 0 1 .4 1 1V20c0 .6-.4 1-1 1A17 17 0 013 4c0-.6.4-1 1-1h3.5c.6 0 1 .4 1 1 0 1.3.2 2.5.6 3.6.1.3 0 .7-.2 1z"/></svg>
    555 201 4478
  </div>
  <nav class="main-nav"><span>Company</span><span>Service Area</span><span>Services</span><span>Gallery</span><span>FAQs</span><span>Contact</span></nav>
</header>

<section class="hero" role="img" aria-label="Smiling electrician in a cap working at an electrical panel"></section>
<svg class="arrow" style="left:96px" width="44" height="76" viewBox="0 0 44 76"><path d="M40 2L4 38l36 36" fill="none" stroke="#fff" stroke-width="3"/></svg>
<svg class="arrow" style="left:1062px" width="44" height="76" viewBox="0 0 44 76"><path d="M4 2l36 36-36 36" fill="none" stroke="#fff" stroke-width="3"/></svg>
<h1 class="hero-title"><span class="light">BRAMBLECOURT</span><span class="bold">ELECTRIC</span></h1>
<p class="hero-lead">Lorem ipsum dolor sit amet, conseetur adipiscing elit, sed do eiusmod tempor incididunt</p>
<div class="btn" style="left:160px;top:434px">Learn more ›</div>
<svg class="abs" style="left:592px;top:525px" width="16" height="106" viewBox="0 0 16 106"><path d="M9 0L3 12h5l-2 10 7-13H8z" fill="#fff"/><line x1="8" y1="30" x2="8" y2="106" stroke="#fff" stroke-width="1.5" stroke-dasharray="3 3"/></svg>

<div class="info" style="left:100px;background:var(--blue)">
  <svg width="44" height="44" viewBox="0 0 44 44" fill="none" stroke="#fff" stroke-width="2"><rect x="8" y="8" width="28" height="34"/><path d="M4 42h36M14 14h4M22 14h4M14 22h4M22 22h4M14 30h4M22 30h4M18 42v-6h8v6M12 8V3h20v5"/></svg>
  <h3>Company</h3><p>In malesuada orci vel sem luctus dapibus. Nulla viverra nibh ac elit placerat, et venenatis metus cursus.</p>
</div>
<div class="info" style="left:433px;background:var(--red)">
  <svg width="50" height="50" viewBox="0 0 50 50" fill="none" stroke="#fff" stroke-width="2"><path d="M4 46l6-28h10M30 18h10l6 28z"/><path d="M25 4a8 8 0 00-8 8c0 7 8 16 8 16s8-9 8-16a8 8 0 00-8-8z"/><circle cx="25" cy="12" r="3"/></svg>
  <h3>Service Area</h3><p>In malesuada orci vel sem luctus dapibus. Nulla viverra nibh ac elit placerat, et venenatis metus cursus.</p>
</div>
<div class="info" style="left:766px;background:var(--ink)">
  <svg width="44" height="44" viewBox="0 0 24 24" fill="none" stroke="#fff" stroke-width="1.3"><path d="M6.6 10.8a15 15 0 006.6 6.6l2.2-2.2c.3-.3.7-.4 1-.2 1.1.4 2.3.6 3.6.6.6 0 1 .4 1 1V20c0 .6-.4 1-1 1A17 17 0 013 4c0-.6.4-1 1-1h3.5c.6 0 1 .4 1 1 0 1.3.2 2.5.6 3.6.1.3 0 .7-.2 1z"/><path d="M15 3a6 6 0 016 6M15 6a3 3 0 013 3"/></svg>
  <h3>Contact</h3><p>14720 Larkspur Ave NE<br>Fernhollow, MN 55099</p><p style="margin-top:10px">555 201 4478</p>
</div>

<div class="welcome-frame"></div>
<div class="ph welcome-photo" role="img" aria-label="Electrician on a ladder drilling into a ceiling"></div>
<div class="abs" style="left:612px;top:936px;width:490px">
  <div class="eyebrow">Welcome to</div>
  <h2 class="section-title" style="font-size:46px;line-height:1.15;margin-bottom:12px;white-space:nowrap"><span class="b">Bramblecourt Electric</span></h2>
  <p class="body-copy" style="font-size:15px">Lorem ipsum dolor sit amet, consectetur adipiscg elit, sed do eiusmod tempor incididunt ut labore et dolore maiqua. Quis ipsum suspendisse ultrices gravida. Risus commodo viverra maecenas accumsan lacus vel facilisis.</p>
</div>
<div class="btn" style="left:612px;top:1165px">Read more ›</div>

<svg class="abs" style="left:0;top:1310px" width="1200" height="1080" viewBox="0 0 1200 1080" preserveAspectRatio="none">
  <path d="M0 40C250-5 420 15 650 40S1000 70 1200 0V90C1000 150 800 110 600 90S250 70 0 50Z" fill="var(--red)"/>
  <path d="M0 45C250 10 430 40 650 65S1000 95 1200 20V960C1000 1070 700 1040 450 1000S150 960 0 1000Z" fill="var(--blue)"/>
  <path d="M0 1000C150 950 350 980 500 1010S900 1080 1200 960V1010C900 1110 600 1070 450 1040S150 990 0 1040Z" fill="var(--red)"/>
</svg>

<div class="abs" style="left:100px;top:1540px;width:460px;color:#fff">
  <h2 style="font-family:'Oswald',sans-serif;font-size:50px;text-transform:uppercase;line-height:1.1;margin-bottom:12px"><span style="font-weight:300">Our</span> <b>Services</b></h2>
  <p style="font-size:15.5px;line-height:1.75">Lorem ipsum dolor sit amet, consectetur adipiscg elit, sed do eiusmod tempor incididunt ut labore et dolore maiqua. Quis ipsum suspendisse ultrices</p>
</div>
<div class="btn" style="left:100px;top:1720px">Read more ›</div>

<div class="service-card" style="left:610px;top:1487px;background:linear-gradient(135deg,#6d6253,#8a8070 50%,#5c5448)" role="img" aria-label="Hands testing wires in a breaker panel">
  <svg width="60" height="60" viewBox="0 0 60 60" fill="none" stroke="#fff" stroke-width="2.5"><path d="M12 48l26-26M42 8a10 10 0 00-4 14l4 4a10 10 0 0014-4l-6-1-3-3-1-6z"/><path d="M10 10l10 4 28 28-6 6-28-28z"/></svg>
  <span>Commerical Electrical<br>Services</span>
</div>
<div class="service-card" style="left:100px;top:1854px;background:linear-gradient(135deg,#9a9a98,#7a7a78 50%,#5a5a58)" role="img" aria-label="Electrician in a hard hat installing a ceiling fixture">
  <svg width="60" height="60" viewBox="0 0 60 60" fill="none" stroke="#fff" stroke-width="2.5"><rect x="6" y="8" width="24" height="34" rx="2"/><path d="M20 14l-6 10h6l-4 10"/><path d="M36 8v10M48 8v10M32 18h20v8a10 10 0 01-20 0zM42 36v14"/></svg>
  <span>Residential Electrical<br>Services</span>
</div>
<div class="service-card" style="left:610px;top:1854px;background:linear-gradient(135deg,#4b4f52,#6f7478 50%,#3d4144)" role="img" aria-label="Electrician with a tablet beside an industrial control cabinet">
  <svg width="60" height="60" viewBox="0 0 60 60" fill="none" stroke="#fff" stroke-width="2.5"><path d="M30 4L18 56M30 4l12 52M10 16h40M14 28h32M22 40h16M22 16l16 12M38 16L22 28M22 40l20 16M38 40L18 56"/></svg>
  <span>Industrial Electrical<br>Services</span>
</div>

<div class="abs" style="left:100px;top:2490px;width:480px">
  <h2 class="section-title" style="font-size:50px;line-height:1.1;margin-bottom:10px"><span class="l" style="color:var(--red)">Service</span> <span class="b">Area</span></h2>
  <p class="body-copy" style="font-size:15px">Lorem ipsum dolor sit amet, constur adipiscg elit, sed do eiusmod tempor incididunt ut labore et dolore mua. Quis ipsum suspendisse ultrices</p>
</div>
<div class="area-list">
  <div><svg width="24" height="20" viewBox="0 0 24 20"><path fill="var(--blue)" d="M0 4l7-3 10 3 7-3v15l-7 3-10-3-7 3z"/><circle cx="12" cy="8" r="4" fill="#fff"/></svg>Chisago MN</div>
  <div><svg width="24" height="20" viewBox="0 0 24 20"><path fill="var(--blue)" d="M0 4l7-3 10 3 7-3v15l-7 3-10-3-7 3z"/><circle cx="12" cy="8" r="4" fill="#fff"/></svg>Pine MN</div>
  <div><svg width="24" height="20" viewBox="0 0 24 20"><path fill="var(--blue)" d="M0 4l7-3 10 3 7-3v15l-7 3-10-3-7 3z"/><circle cx="12" cy="8" r="4" fill="#fff"/></svg>Isanti MN</div>
  <div><svg width="24" height="20" viewBox="0 0 24 20"><path fill="var(--blue)" d="M0 4l7-3 10 3 7-3v15l-7 3-10-3-7 3z"/><circle cx="12" cy="8" r="4" fill="#fff"/></svg>Anoka MN</div>
  <div><svg width="24" height="20" viewBox="0 0 24 20"><path fill="var(--blue)" d="M0 4l7-3 10 3 7-3v15l-7 3-10-3-7 3z"/><circle cx="12" cy="8" r="4" fill="#fff"/></svg>Washington MN</div>
</div>
<div class="btn" style="left:100px;top:2795px">Read more ›</div>
<div class="ph" style="left:595px;top:2484px;width:498px;height:332px;background:radial-gradient(ellipse at center,#e6eef8 0%,#f6f9fd 70%,#fff 100%)" role="img" aria-label="Outline map of the United States with service location pins"></div>

<div class="ph" style="left:0;top:2949px;width:960px;height:506px;background:linear-gradient(90deg,#d8dbdc 0%,#b9bbbc 30%,#e4e1dc 55%,#9d9894 80%,#c9c5bf 100%)" role="img" aria-label="Electrician in a hard hat and safety glasses using a tablet beside a fuse board"></div>
<form class="quote">
  <h3>Request a <b>free quote</b></h3>
  <div class="field">Name</div><div class="field">Email</div><div class="field">Phone</div><div class="field">Location</div><div class="field">City</div>
  <div class="quote-btn">GET A QUOTE ›</div>
</form>

<h2 class="section-title abs" style="left:0;top:3525px;width:1200px;text-align:center;font-size:50px"><span class="l" style="color:var(--red)">Latest</span> <span class="b">Project</span></h2>
<div class="ph" style="left:100px;top:3636px;width:241px;height:189px;background:linear-gradient(160deg,#24395e,#4f6b9a 50%,#a8804a)" role="img" aria-label="Large industrial factory floor"></div>
<div class="ph" style="left:353px;top:3713px;width:241px;height:189px;background:linear-gradient(160deg,#d8d4cc,#a89e90 60%,#7a6f62)" role="img" aria-label="Bright living room with a chandelier"></div>
<div class="ph" style="left:607px;top:3636px;width:241px;height:189px;background:linear-gradient(160deg,#c8b8a8,#8b7a6a 60%,#4a3f36)" role="img" aria-label="Hand holding a phone with a smart home app"></div>
<div class="ph" style="left:861px;top:3713px;width:241px;height:189px;background:linear-gradient(160deg,#e6d7a8,#b89a52 50%,#6f5a30)" role="img" aria-label="Row of glowing pendant lights"></div>
<div class="btn" style="left:415px;top:3960px;padding:0 24px">View our all project gallery ›</div>

<footer class="footer">
  <div class="footer-brand"><span class="dot"></span><span>Bramblecourt<br>Electric</span></div>
  <div class="fdiv" style="left:300px"></div>
  <div class="fcol" style="left:328px;top:72px;line-height:1.9"><h4>Contact info</h4>
    <div style="display:flex;gap:8px"><svg width="12" height="16" viewBox="0 0 12 16"><path fill="var(--blue)" d="M6 0a6 6 0 00-6 6c0 4.5 6 10 6 10s6-5.5 6-10a6 6 0 00-6-6zm0 8.5A2.5 2.5 0 116 3.5a2.5 2.5 0 010 5z"/></svg><span>14720 Larkspur Ave NE<br>Fernhollow, MN 55099</span></div>
    <div style="display:flex;gap:8px;align-items:center;margin-top:4px"><svg width="14" height="14" viewBox="0 0 24 24"><path fill="var(--blue)" d="M6.6 10.8a15 15 0 006.6 6.6l2.2-2.2c.3-.3.7-.4 1-.2 1.1.4 2.3.6 3.6.6.6 0 1 .4 1 1V20c0 .6-.4 1-1 1A17 17 0 013 4c0-.6.4-1 1-1h3.5c.6 0 1 .4 1 1 0 1.3.2 2.5.6 3.6.1.3 0 .7-.2 1z"/></svg>555 201 4478</div>
  </div>
  <div class="fdiv" style="left:507px"></div>
  <div class="fcol" style="left:536px;top:72px;line-height:2.3"><h4 style="margin-bottom:6px">Sitemap</h4>› Company<br>› Service Area<br>› Services<br>› Gallery<br>› FAQs<br>› Contact</div>
  <div class="fdiv" style="left:670px"></div>
  <div class="fcol" style="left:698px;top:72px;line-height:2.3"><h4 style="margin-bottom:6px">Services</h4>› Commerical Electrical Services<br>› Residential Electrical Services<br>› Industrial Electrical Services</div>
  <div class="fdiv" style="left:952px"></div>
  <div class="fcol" style="left:980px;top:72px"><h4>Follow us</h4><div class="social"><span></span><span></span><span></span></div></div>
  <div class="abs" style="left:100px;top:352px;width:1000px;height:1px;background:#555"></div>
  <div class="abs" style="left:0;top:372px;width:1200px;text-align:center;font-size:14px">© 2022 <span style="color:var(--blue)">Bramblecourt Electric</span>. All right reserved</div>
</footer>

</body>
</html>
```